OTV Web Design Project

I'm looking for a small, friendly,functional, information based website. If you go through the attachments, you would know the nature of the business.
Updates

Hi,

I have uploaded a picture of the CEO, Mr. Darvesh Kolhi NAMPQ member. Please feel free to use it whereever appropriate.

Thanks!

Hello, I have uploaded some references. I like the colours used on the bar and would w

Example of a we page . I like this layout for the inside pages.

I am changing the tabs on my website to:

Home
About us
Services
Contact us

The services tab will have three sub pages:

Immigration
Education
AccommodationAccommodation

Target Market(s)

Young international students willing to come to Canada to study, young international students willing to immigrate to Canada, parents of the students

Industry/Entity Type

Business

Requirements
Must have
• OTV HOME
ABOUT US
CONTACT
SERVICES
TAG LINE

The website should look n feel trendy, smart, current, factual, trustworthy etc....
Nice to have
• I am looking for a bold, attractive, eye catchy home page with less text! Something that makes a statement....
Should not have
• No Clip art, flash animation, no bells n whistles please

```html
<!DOCTYPE html>
<html lang="en">
<head>
<meta charset="utf-8">
<title>OTV – Northway Advisory Group</title>
<link rel="stylesheet" href="https://fonts.googleapis.com/css2?family=Ubuntu:wght@400;500;700&family=Didact+Gothic&display=swap">
<style>
  :root {
    --red: #ff0000;
    --red-deep: #d80000;
    --red-light: #ff3b3b;
    --ink: #111111;
    --text-grey: #6e6e6e;
    --nav-grey: #6a6a6a;
    --page-bg: #e9e9e9;
    --band-bg: #d6d6d6;
    --panel-white: #ffffff;
    --mission-bg: #efefef;
    --rule-dark: #4a4a4a;
    --footer-link: #ffb3a0;
  }
  * { box-sizing: border-box; margin: 0; padding: 0; }
  html, body { width: 1200px; height: 885px; overflow: hidden; }
  body {
    background: linear-gradient(var(--band-bg) 0 215px, var(--page-bg) 215px 100%);
    font-family: "Ubuntu", sans-serif;
  }
  .site {
    position: absolute; left: 114px; top: 0; width: 967px; height: 737px;
    background: var(--panel-white);
    box-shadow: 0 0 6px rgba(0,0,0,0.18);
  }
  .top-strip { position: absolute; left: 0; top: 0; width: 100%; height: 17px; background: var(--red); }
  .header { position: absolute; left: 0; top: 17px; width: 100%; height: 159px; }
  .brand { position: absolute; left: 33px; top: 58px; display: flex; align-items: center; gap: 10px; }
  .brand-mark { width: 22px; height: 22px; background: var(--red); }
  .brand-name { font-family: "Ubuntu", sans-serif; font-weight: 700; font-size: 26px; color: var(--text-grey); line-height: 1; }
  .brand-name small { display: block; font-size: 18px; margin-top: 6px; }
  .tagline {
    position: absolute; left: 309px; top: 62px;
    font-family: "Ubuntu", sans-serif; font-weight: 700; font-size: 31px; color: var(--red); letter-spacing: 0.3px;
  }
  .hero-photo {
    position: absolute; right: 0; top: 0; width: 263px; height: 215px;
    background: linear-gradient(120deg, #f3e3d6 0%, #d9a98a 45%, #b88059 75%, #eadfd8 100%);
  }
  .nav {
    position: absolute; left: 0; top: 176px; width: 100%; height: 39px;
    display: flex; list-style: none;
    background: linear-gradient(#f6f6f6, #e2e2e2);
    border-bottom: 1px solid #cfcfcf;
  }
  .nav li { display: flex; align-items: center; justify-content: center; height: 100%;
    font-family: "Didact Gothic", sans-serif; font-size: 17px; color: var(--nav-grey); letter-spacing: 0.2px; }
  .nav .active { background: linear-gradient(var(--red-light), var(--red-deep)); color: #fff; width: 157px; }
  .nav li:nth-child(2) { width: 170px; }
  .nav li:nth-child(3) { width: 195px; }
  .nav li:nth-child(4) { width: 190px; }
  .nav li:nth-child(5) { flex: 1; background: rgba(230,230,230,0.55); }
  .services { position: absolute; left: 0; top: 215px; width: 100%; height: 242px; }
  .service { position: absolute; top: 42px; width: 240px; }
  .service:nth-child(1) { left: 54px; }
  .service:nth-child(2) { left: 365px; }
  .service:nth-child(3) { left: 683px; }
  .section-title { font-family: "Ubuntu", sans-serif; font-weight: 500; font-size: 15.5px; color: var(--ink); letter-spacing: 0.3px; }
  .body-text { font-size: 12.8px; line-height: 19.4px; color: var(--text-grey); letter-spacing: 0.2px; }
  .service .body-text { margin-top: 13px; width: 235px; }
  .btn {
    display: inline-flex; align-items: center; justify-content: center;
    margin-top: 16px; width: 115px; height: 33px; border-radius: 3px;
    background: linear-gradient(var(--red-light), var(--red-deep));
    box-shadow: 0 1px 3px rgba(0,0,0,0.3);
    color: #fff; font-size: 14px;
  }
  .mission { position: absolute; left: 0; top: 457px; width: 100%; height: 169px; background: var(--mission-bg); padding: 40px 54px 0; }
  .mission .body-text { margin-top: 14px; width: 860px; }
  .footer-rule { position: absolute; left: 0; top: 626px; width: 100%; height: 6px; background: var(--rule-dark); }
  .footer {
    position: absolute; left: 0; top: 632px; width: 100%; height: 105px;
    background: linear-gradient(var(--red-deep), var(--red) 60%, var(--red-light));
    text-align: center;
  }
  .footer-links { margin-top: 29px; font-size: 11.5px; color: var(--footer-link); }
  .footer-links span.sep { color: #fff; margin: 0 11px; }
  .copyright { margin-top: 20px; font-size: 11.5px; color: #fff; }
</style>
</head>
<body>
  <div class="site">
    <div class="top-strip"></div>
    <header class="header">
      <div class="brand">
        <div class="brand-mark"></div>
        <div class="brand-name">OTV<small>Northway Advisory Group</small></div>
      </div>
      <div class="tagline">Dare to Dream Canadian...</div>
    </header>
    <div class="hero-photo" role="img" aria-label="Photo of a smiling young woman talking on a mobile phone"></div>
    <ul class="nav">
      <li class="active">HOME</li>
      <li>ABOUT US</li>
      <li>SERVICES</li>
      <li>OTV MISSION</li>
      <li>CONTACT US</li>
    </ul>
    <section class="services">
      <article class="service">
        <h2 class="section-title">IMMIGRATION</h2>
        <p class="body-text">Canada has been consistently rated by the United Nations as one of the top countries in the world to live, work .......</p>
        <span class="btn">Read More</span>
      </article>
      <article class="service">
        <h2 class="section-title">EDUCATION</h2>
        <p class="body-text">Canada has one of the finest education systems in the world. Every year thousands of students from all over the world .......</p>
        <span class="btn">Read More</span>
      </article>
      <article class="service">
        <h2 class="section-title">STUDENT ACCOMODATION</h2>
        <p class="body-text">Canada has been consistently rated by the United Nations as one of the top countries in the world to live, work .......</p>
        <span class="btn">Read More</span>
      </article>
    </section>
    <section class="mission">
      <h2 class="section-title">OTV MISSION</h2>
      <p class="body-text">At OTV we are committed to our customer centered philosophy. Our mission is to help our clients achieve their goals by providing them with world class customer service that is both reliable and competitively superior. We are driven by our core values: ethics, expertise and leadership. We believe that honesty paves the way for true success. We have been there. We know what it takes.</p>
    </section>
    <div class="footer-rule"></div>
    <footer class="footer">
      <p class="footer-links">Privacy Policy<span class="sep">|</span>Terms Of Use<span class="sep">|</span>Feedback</p>
      <p class="copyright">Copyright © 2014. All Rights Reserved.</p>
    </footer>
  </div>
</body>
</html>
```